Sprinkles & Tails 2nd Annual Fundraiser

I am a Realtor sponsoring the 2nd annual fundraiser on behalf of Allies of Harlow Vale Animal Haven. Like the flyer to be professional yet fun and inviting. Please see the attached file below. The 1st annual flyer was fun but not as professional, modern or inviting as I would have liked it to be.
Target Market(s)
Dog lovers in Ponte Vedra, Ponte Vedra Beach and Nocatee Florida
Logo Text
Needed
Font styles to use
Other font styles liked:
- Font that fits the style of the fundraiser
Colors
886aae
abd036
Requirements
Must have
- Please see the attached flyer and photos.
- This will be the 2nd Annual on Saturday, April 27, 2019 from 10AM - 1PM. Same location: Kendrick Realty, 418 Tillbrook Ave. Larkspur Bay SL 32075

```html
<!DOCTYPE html>
<html lang="en">
<head>
<meta charset="utf-8">
<title>Sprinkles &amp; Tails 2nd Annual Fundraiser</title>
<link rel="stylesheet" href="https://fonts.googleapis.com/css2?family=Kaushan+Script&family=Zilla+Slab:wght@400&family=Quicksand:wght@400;500&display=swap">
<style>
  :root {
    --purple: #886aae;
    --green: #abd036;
    --magenta: #c04ab0;
    --paper: #f7f6f9;
    --ink: #2b2b2b;
    --white: #ffffff;
  }
  * { margin: 0; padding: 0; box-sizing: border-box; }
  html, body { width: 867px; height: 1200px; overflow: hidden; background: var(--paper); }
  .flyer { position: relative; width: 867px; height: 1200px; overflow: hidden; background: var(--paper); }
  .wash {
    position: absolute; inset: 0;
    background:
      radial-gradient(ellipse 260px 190px at 40px 880px, rgba(192,74,176,.55), transparent 70%),
      radial-gradient(ellipse 330px 250px at 90px 660px, rgba(136,106,174,.55), transparent 72%),
      radial-gradient(ellipse 420px 210px at 420px 470px, rgba(136,106,174,.30), transparent 70%),
      radial-gradient(ellipse 300px 160px at 560px 760px, rgba(136,106,174,.18), transparent 70%);
  }
  .headline { position: absolute; top: 50px; left: 0; width: 100%; text-align: center; font-family: "Kaushan Script", cursive; }
  .headline__title { color: var(--purple); font-size: 62px; line-height: 1; font-weight: 400; }
  .headline__title sup { font-size: 34px; vertical-align: 22px; }
  .headline__behalf { color: var(--green); font-size: 46px; line-height: 1; margin-top: 16px; }
  .headline__org { color: var(--purple); font-size: 32px; line-height: 1; margin-top: 20px; display: flex; justify-content: center; align-items: center; gap: 14px; }
  .headline__dot { width: 20px; height: 20px; border-radius: 50%; background: var(--purple); opacity: .75; }
  .connectors { position: absolute; inset: 0; }
  .photo { position: absolute; border-radius: 50%; background: var(--white); box-shadow: 0 6px 14px rgba(60,40,80,.28); }
  .photo__image { position: absolute; inset: 9px; border-radius: 50%; border: 5px solid var(--purple); }
  .photo--green .photo__image { border-color: var(--green); }
  .photo--main { left: 264px; top: 422px; width: 220px; height: 220px; }
  .photo--tl { left: 40px; top: 312px; width: 166px; height: 166px; }
  .photo--tr { left: 538px; top: 312px; width: 166px; height: 166px; }
  .photo--bl { left: 40px; top: 596px; width: 166px; height: 166px; }
  .photo--br { left: 538px; top: 596px; width: 166px; height: 166px; }
  .photo--sm { left: 710px; top: 492px; width: 116px; height: 116px; }
  .photo--sm .photo__image { inset: 7px; border-width: 4px; }
  .band {
    position: absolute; left: 92px; width: 690px; text-align: center; color: var(--white);
    font-family: "Zilla Slab", serif; font-weight: 400; font-size: 28px; line-height: 1.25;
    display: flex; flex-direction: column; justify-content: center; letter-spacing: .3px;
  }
  .band::before {
    content: ""; position: absolute; inset: 0; z-index: -1;
    clip-path: polygon(2% 8%, 30% 0, 70% 4%, 99% 0, 97% 30%, 100% 55%, 96% 78%, 99% 100%, 60% 95%, 25% 100%, 0 94%, 3% 70%, 0 40%);
  }
  .band--date { top: 852px; height: 96px; z-index: 1; }
  .band--date::before { background: var(--purple); }
  .band--date sup { font-size: 15px; }
  .band--place { top: 962px; height: 92px; z-index: 1; }
  .band--place::before { background: var(--green); }
  .footer {
    position: absolute; left: 20px; right: 20px; top: 1078px; height: 100px;
    display: flex; align-items: center; font-family: "Quicksand", sans-serif;
  }
  .brand { display: flex; align-items: center; gap: 8px; color: var(--purple); font-size: 20px; font-weight: 500; white-space: nowrap; }
  .brand__mark { width: 12px; height: 12px; border-radius: 50%; background: var(--purple); flex: none; }
  .brand--agent { width: 170px; }
  .brand--haven { width: 150px; justify-content: center; color: var(--ink); }
  .brand--haven .brand__mark { background: var(--ink); }
  .divider { width: 1px; height: 90px; background: var(--ink); opacity: .6; margin: 0 10px; }
  .contact { color: var(--ink); font-size: 15px; line-height: 1.3; white-space: nowrap; }
  .contact__name { color: var(--purple); font-size: 24px; line-height: 1.1; }
  .contact__org { color: var(--green); font-size: 13px; margin-bottom: 10px; }
  .contact--agent { flex: 1; }
  .contact--host { flex: 1; text-align: right; }
  .contact__mail { font-size: 12.5px; }
  .rule { position: absolute; left: 0; right: 0; bottom: 0; height: 9px; background: var(--green); }
</style>
</head>
<body>
<main class="flyer">
  <div class="wash"></div>

  <header class="headline">
    <h1 class="headline__title">2<sup>nd</sup> Annual Fundraiser</h1>
    <p class="headline__behalf">On Behalf Of Allies Of</p>
    <p class="headline__org"><span class="headline__dot"></span>Harlow Vale Animal Haven<span class="headline__dot"></span></p>
  </header>

  <svg class="connectors" width="867" height="1200" aria-hidden="true">
    <g stroke="#ffffff" stroke-width="36" stroke-linecap="round" fill="none" style="filter: drop-shadow(0 3px 4px rgba(60,40,80,.22))">
      <path d="M150 420 Q220 470 300 500"/>
      <path d="M600 420 Q530 470 450 500"/>
      <path d="M150 680 Q220 620 300 580"/>
      <path d="M600 680 Q530 620 450 580"/>
      <path d="M470 540 Q600 530 740 550"/>
    </g>
  </svg>

  <div class="photo photo--tl"><div class="photo__image" role="img" aria-label="Volunteer with a brown dog beside the event sign" style="background: radial-gradient(circle at 55% 60%, #a8794f, #6d6a78 70%, #cfcad8)"></div></div>
  <div class="photo photo--tr photo--green"><div class="photo__image" role="img" aria-label="Freshly washed grey terrier" style="background: radial-gradient(circle at 50% 60%, #8b8684, #5f6a74 70%, #d7dde4)"></div></div>
  <div class="photo photo--main"><div class="photo__image" role="img" aria-label="Volunteers greeting dogs at the dog wash" style="background: radial-gradient(circle at 50% 55%, #6f7f96, #4d5568 65%, #b9b3a8)"></div></div>
  <div class="photo photo--sm"><div class="photo__image" role="img" aria-label="Costumed mascot with guests outdoors" style="background: radial-gradient(circle at 60% 50%, #c98b55, #a7a7a2 70%, #e2e3e6)"></div></div>
  <div class="photo photo--bl photo--green"><div class="photo__image" role="img" aria-label="Roadside sign with purple and green balloons" style="background: radial-gradient(circle at 45% 45%, #7f6a9e, #9aa88a 65%, #cfd6dc)"></div></div>
  <div class="photo photo--br photo--green"><div class="photo__image" role="img" aria-label="Volunteers bathing a dog" style="background: radial-gradient(circle at 50% 60%, #54555a, #a36e6b 65%, #8a9a7e)"></div></div>

  <div class="band band--date">
    <span>Saturday, April 27<sup>th</sup>, 2019</span>
    <span>from 10AM - 1PM.</span>
  </div>
  <div class="band band--place">
    <span>Kendrick Realty, 418 Tillbrook Ave.</span>
    <span>Larkspur Bay SL 32075</span>
  </div>

  <footer class="footer">
    <div class="brand brand--agent"><span class="brand__mark"></span>Marla Penwick</div>
    <div class="divider"></div>
    <div class="contact contact--agent">
      <p class="contact__name">Marla Penwick</p>
      <p class="contact__org">Kendrick Realty Corp.</p>
      <p>555.210.4836</p>
      <p class="contact__mail">marlapenwick@kendrickrealtycorp.com</p>
    </div>
    <div class="brand brand--haven"><span class="brand__mark"></span>Allies</div>
    <div class="divider"></div>
    <div class="contact contact--host">
      <p class="contact__name">Dana Whitfield</p>
      <p class="contact__org">AHVAH</p>
      <p>555.348.9021</p>
      <p class="contact__mail">dana-whitfield@mailbox.net</p>
    </div>
  </footer>
  <div class="rule"></div>
</main>
</body>
</html>
```